Book Cover Design Project - Lesbian stories

I need a cover for my ebook of short stories. Target market is lesbians. I want something erotic (but not too over the top or porny). Something tasteful and feminine. For example two women with a flower see artist Mirel Dunstan http://www.galvoristudio.example/magazine/article.php?articleID=287.

Title: Harbour Letters, Paper Moons

By Lucinda Marvaro

```html
<!DOCTYPE html>
<html lang="en">
<head>
<meta charset="utf-8">
<title>Harbour Letters, Paper Moons — Lucinda Marvaro</title>
<link rel="stylesheet" href="https://fonts.googleapis.com/css2?family=Cinzel:wght@500&family=Great+Vibes&family=Poppins:wght@600&display=swap">
<style>
  :root {
    --page: #ffffff;
    --ink-white: #ffffff;
    --script-pink: #ee4f9c;
    --title-orange: #f6ae3c;
    --title-red: #f04848;
    --photo-dark: #17100e;
    --photo-mid: #6b4a3a;
    --photo-tan: #c79d7c;
    --photo-warm: #a5774f;
  }
  * { margin: 0; padding: 0; box-sizing: border-box; }
  html, body {
    width: 1000px; height: 1200px; overflow: hidden;
    background: var(--page);
  }
  .cover {
    position: absolute; left: 170px; top: 96px;
    width: 678px; height: 1016px; overflow: hidden;
  }
  .cover-photo {
    position: absolute; inset: 0;
    background:
      radial-gradient(ellipse 190px 230px at 300px 250px, var(--photo-dark) 0%, rgba(23,16,14,0.85) 45%, rgba(23,16,14,0) 100%),
      radial-gradient(ellipse 160px 260px at 90px 420px, rgba(230,200,180,0.55), rgba(230,200,180,0) 100%),
      radial-gradient(ellipse 260px 300px at 600px 200px, var(--photo-warm), rgba(165,119,79,0) 100%),
      radial-gradient(ellipse 300px 260px at 330px 900px, rgba(23,16,14,0.7), rgba(23,16,14,0) 100%),
      linear-gradient(180deg, var(--photo-mid) 0%, var(--photo-tan) 55%, var(--photo-mid) 100%);
  }
  .author {
    position: absolute; top: 36px; left: 0; width: 100%;
    text-align: center;
    font-family: "Cinzel", serif; font-weight: 500;
    font-size: 50px; letter-spacing: 4px;
    color: var(--ink-white);
  }
  .title { position: absolute; inset: 0; }
  .title span { position: absolute; white-space: nowrap; line-height: 1; }
  .initial {
    font-family: "Great Vibes", cursive;
    color: var(--script-pink);
    font-size: 330px;
  }
  .initial-h { left: 10px; top: 380px; }
  .initial-p { left: 70px; top: 700px; }
  .word {
    font-family: "Poppins", sans-serif; font-weight: 600;
    font-size: 72px; letter-spacing: -1px;
  }
  .word-orange { color: var(--title-orange); }
  .word-red { color: var(--title-red); }
  .line-1 { left: 258px; top: 538px; }
  .line-2 { left: 290px; top: 618px; font-size: 64px; }
  .line-3 { left: 350px; top: 722px; }
  .line-4 { left: 340px; top: 806px; display: flex; align-items: flex-start; }
  .venus-pair { width: 104px; height: 120px; margin: 4px 0 0 0; }
</style>
</head>
<body>
  <main class="cover">
    <div class="cover-photo" role="img" aria-label="Soft-focus warm photograph of two women embracing, dark hair framing the centre"></div>
    <p class="author">Lucinda Marvaro</p>
    <h1 class="title" aria-label="Harbour Letters, Paper Moons">
      <span class="initial initial-h">H</span>
      <span class="word word-orange line-1">ARBOUR</span>
      <span class="word word-orange line-2">LETTERS,</span>
      <span class="initial initial-p">P</span>
      <span class="word word-red line-3">APER</span>
      <span class="word word-red line-4">M<svg class="venus-pair" viewBox="0 0 104 120" aria-hidden="true">
          <g fill="none" stroke="var(--script-pink)" stroke-width="10">
            <circle cx="33" cy="33" r="24"/>
            <circle cx="71" cy="33" r="24"/>
            <line x1="33" y1="57" x2="33" y2="112"/>
            <line x1="16" y1="88" x2="50" y2="88"/>
            <line x1="71" y1="57" x2="71" y2="112"/>
            <line x1="54" y1="88" x2="88" y2="88"/>
          </g>
        </svg>NS</span>
    </h1>
  </main>
</body>
</html>
```